Football tournament flyer

I would like a quick turn around for this please.
I need a flyer to promote an 11 aside football tournament I am organising to celebrate the 23rd independence of my country Somaliland. Please use the national colours of our flag in the flyer, I have attached a file for your consideration.
The tournament will take place on 10/05/2014, from 9am - 8pm. The venue will be Corrin Open Space, Tavistrel Lane, Enfield, EN7 2QR.
Refreshments, food and entertainment will be provided.
The name of the cup is Warsadle Cup.
Spaces are limited and the entry fee per team is £200. All proceeds are for charity projects in Somaliland.
To register a team contact Faisal Warsame on 07521 804 192 or Bashir Yusuf on 07463 125 870.
The best players will have the opportunity to represent Somaliland in an international game on the 17/05/2014.
The tournament is organised by Dalmar FC and EverKindred Foundation.

```html
<!DOCTYPE html>
<html lang="en">
<head>
<meta charset="utf-8">
<title>Warsadle Cup 2014 – Football Tournament Flyer</title>
<link rel="stylesheet" href="https://fonts.googleapis.com/css2?family=Audiowide&family=Arvo:wght@400;700&family=Cabin:ital,wght@0,500;0,600;1,700&family=Kaushan+Script&family=Tinos:ital,wght@0,400;0,700;1,700&display=swap">
<style>
  :root {
    --black: #050302;
    --flag-green: #1e8a3c;
    --flag-white: #f2f2f2;
    --flag-red: #d9141f;
    --fire-red: #b3210c;
    --fire-orange: #e8611a;
    --fire-deep: #4a0b04;
    --yellow: #f7e84a;
    --gold: #f3d23a;
    --lime: #c9de2c;
    --cup-red: #e01b1b;
    --badge-red: #e3202a;
    --white: #ffffff;
    --ball-light: #e9ecef;
    --ball-blue: #3b78b8;
  }
  * { box-sizing: border-box; margin: 0; padding: 0; }
  html, body { width: 848px; height: 1200px; overflow: hidden; background: var(--black); }
  .flyer {
    position: relative;
    width: 848px;
    height: 1200px;
    overflow: hidden;
    background: var(--black);
  }
  .fire-backdrop {
    position: absolute; left: 0; top: 250px; width: 848px; height: 550px;
    background:
      radial-gradient(ellipse 340px 260px at 620px 300px, var(--fire-orange) 0%, var(--fire-red) 40%, transparent 80%),
      radial-gradient(ellipse 300px 220px at 250px 200px, var(--fire-red) 0%, var(--fire-deep) 60%, transparent 90%),
      radial-gradient(ellipse 420px 200px at 420px 480px, var(--fire-red) 0%, transparent 80%),
      var(--black);
  }
  .fire-lower {
    position: absolute; left: 0; top: 960px; width: 848px; height: 240px;
    background:
      radial-gradient(ellipse 380px 180px at 560px 120px, var(--fire-red) 0%, var(--fire-deep) 55%, transparent 90%),
      radial-gradient(ellipse 260px 160px at 180px 200px, var(--fire-deep) 0%, transparent 80%),
      var(--black);
  }
  .flag-banner {
    position: absolute; left: 0; top: 0; width: 848px; height: 150px;
    background: linear-gradient(172deg, var(--flag-green) 0%, var(--flag-green) 18%, var(--flag-white) 30%, var(--flag-white) 45%, var(--flag-red) 58%, var(--fire-deep) 80%, var(--black) 100%);
    opacity: .85;
  }
  .presenters {
    position: absolute; left: 0; top: 118px; width: 848px; text-align: center;
    font: 500 29px "Cabin", sans-serif; color: var(--yellow);
  }
  .cup-name {
    position: absolute; left: 0; width: 848px; text-align: center;
    font: 400 80px/1 "Audiowide", sans-serif; color: var(--cup-red);
    -webkit-text-stroke: 2px #3a0a06;
    text-shadow: 0 0 0 var(--gold), 2px 2px 0 #f0c93a, -2px -2px 0 #6b4b10;
    letter-spacing: 2px;
  }
  .cup-name--title { top: 184px; }
  .cup-name--cup { top: 274px; left: -12px; }
  .cup-year {
    position: absolute; left: 542px; top: 252px;
    font: 700 58px "Cabin", sans-serif; color: var(--lime);
    transform: rotate(-10deg);
    -webkit-text-stroke: 1px #5b6a10;
  }
  .date-month, .date-day, .date-time {
    position: absolute; font-family: "Arvo", serif; color: var(--yellow); font-weight: 700;
  }
  .date-month { left: 52px; top: 304px; font-size: 54px; }
  .date-day { left: 44px; top: 340px; font-size: 150px; font-weight: 400; line-height: 1; }
  .date-time { left: 52px; top: 500px; font-size: 26px; }
  .ball-art {
    position: absolute; left: 205px; top: 462px; width: 310px; height: 310px; border-radius: 50%;
    background: radial-gradient(circle at 40% 35%, var(--ball-light) 0%, #b9c0c8 55%, #2a2f35 90%, var(--fire-orange) 100%);
  }
  .kick-silhouette {
    position: absolute; left: 520px; top: 370px; width: 200px; height: 220px;
    background: radial-gradient(ellipse at 50% 55%, var(--yellow) 0%, rgba(247,232,74,.6) 45%, transparent 72%);
  }
  .runner-silhouette {
    position: absolute; left: 0; top: 860px; width: 140px; height: 260px;
    background: radial-gradient(ellipse at 50% 45%, #1c2f5e 0%, #0c1630 55%, transparent 80%);
  }
  .entry-badge {
    position: absolute; left: 38px; top: 648px; width: 194px; height: 104px;
    background: var(--badge-red); border-radius: 10px; color: var(--white);
    text-align: center; box-shadow: 0 3px 8px rgba(0,0,0,.6);
  }
  .entry-label { font: 500 20px "Cabin", sans-serif; padding-top: 12px; }
  .entry-price { font: 600 44px/1.1 "Cabin", sans-serif; }
  .selection-note {
    position: absolute; left: 510px; top: 640px; width: 350px; text-align: center;
    font: 400 20px/1.27 "Tinos", serif; color: var(--white);
    text-shadow: 0 0 4px #000, 0 0 2px #000;
  }
  .venue-band {
    position: absolute; left: 0; top: 800px; width: 848px; height: 180px;
    background: linear-gradient(var(--black) 0%, var(--black) 80%, transparent 100%);
  }
  .venue-divider {
    position: absolute; left: 136px; width: 584px; border-top: 3px dashed var(--gold);
  }
  .venue-divider--top { top: 820px; }
  .venue-divider--bottom { top: 915px; }
  .venue-name {
    position: absolute; left: 0; top: 822px; width: 848px; text-align: center;
    font: 400 44px "Tinos", serif; color: var(--yellow); letter-spacing: 1px;
  }
  .venue-address {
    position: absolute; left: 0; top: 874px; width: 848px; text-align: center;
    font: 400 28px "Tinos", serif; color: var(--yellow); letter-spacing: 1px;
  }
  .venue-details {
    position: absolute; left: 0; top: 926px; width: 848px; text-align: center;
    font: 400 20px/1.27 "Tinos", serif; color: var(--white);
  }
  .registration {
    position: absolute; left: 194px; top: 1032px;
    font-family: "Tinos", serif; color: var(--yellow); text-shadow: 0 0 4px #000;
  }
  .registration-lead { font-size: 24px; font-weight: 700; font-style: italic; padding-left: 6px; }
  .contact { display: flex; font-size: 24px; font-weight: 700; line-height: 1.25; }
  .contact-name { width: 176px; }
</style>
</head>
<body>
<main class="flyer">
  <div class="fire-backdrop" role="img" aria-label="Flames and lightning background"></div>
  <div class="fire-lower" role="img" aria-label="Smouldering flames background"></div>
  <div class="flag-banner" role="img" aria-label="Brushed Somaliland flag in green, white and red with black star"></div>

  <p class="presenters">Dalmar FC and EverKindred Foundation Present</p>
  <h1 class="cup-name cup-name--title">WARSADLE</h1>
  <p class="cup-name cup-name--cup">CUP</p>
  <p class="cup-year">2014</p>

  <p class="date-month">MAY</p>
  <p class="date-day">10</p>
  <p class="date-time">9 AM - 8PM</p>

  <div class="ball-art" role="img" aria-label="Football splashed with water and wrapped in flames"></div>
  <div class="kick-silhouette" role="img" aria-label="Yellow silhouette of a player doing a bicycle kick"></div>

  <div class="entry-badge">
    <p class="entry-label">Entry Fee Per Team</p>
    <p class="entry-price">£200</p>
  </div>

  <p class="selection-note">The best players will have<br>the opportunity to represent<br>Somaliland in an<br>international game on the<br>17/05/2014</p>

  <div class="venue-band"></div>
  <div class="venue-divider venue-divider--top"></div>
  <p class="venue-name">CORRIN OPEN SPACE</p>
  <p class="venue-address">Tavistrel Lane, Enfield, EN7 2QR</p>
  <div class="venue-divider venue-divider--bottom"></div>
  <p class="venue-details">With refreshments, food and entertainment<br>All proceeds are for charity projects in Somaliland</p>

  <div class="runner-silhouette" role="img" aria-label="Backlit silhouette of a player kicking a ball"></div>

  <section class="registration">
    <p class="registration-lead">To register a team please contact:</p>
    <p class="contact"><span class="contact-name">Faisal Warsame</span><span>: 07521 804 192</span></p>
    <p class="contact"><span class="contact-name">Bashir Yusuf</span><span>: 07463 125 870</span></p>
  </section>
</main>
</body>
</html>
```